Create a Dynamic, Connecting, Professional looking PowerPoint Design master for our company.

Power point design

Target Market: High worth individuals and corporate group
Industry: Sport and services

Landscape format

Should include various slide such as:
Introduction page (photo background- inclusive logo)
Company presentation (with photos of various projects)
Different slide layouts to place general information with large photo & logo (in different sizes) as well as standard elements, such as text boxes, lines, default shapes, etc
Timeline page
Table pages
Various infographic style pages with editable chart
Our service page – Icons
Location page (world map)
Comparaison pages (3 offers to compare)
Closing page – thank you & contact
Page numbering

Colors:
#6ea6fa
#517ed8
#3758b4
#203390
#060d6c
#2EC193
White / Grey and black

Fonts:
Work sans / Helveticanow / Or other suitable.
Creative use of the logo in the slides. The Tirem icon may be used as a small device or large watermark to enhance branding.

The uploaded photos are indicative of the ones that we would like to use (ie: sail racing) there are here for you to include in the design but would need to be easily replaceable by the final photos we would be using.

If you have any questions or need any aditional material, please send me a message and I will try to respond to it as quickly as possible (bearing in mind that my time zone is UTC +2)

Target Market(s)

High worth individuals and corporate groups

Industry/Entity Type

Sport and services (sailing)

Font styles to use
Other font styles liked:
• Work Sans / Helveticanow

Colors
0054AA
0677BA
7BADD7
CADEEF
E8F1F8
00AB8E
00BBA5
67D7C9
C6EFE9
E9F9F6

Requirements
Must have
• Introduction page (photo background- inclusive logo) Company presentation (with photos of various projects) Different slide layouts to place general information with large photo & logo (in different sizes) as well as standard elements, such as text boxes, lines, default shapes, etc Timeline page Table pages Various infographic style pages with editable chart Our service page – Icons Location page (world map) Comparaison pages (3 offers to compare) Closing page – thank you & contact Page numbering
Nice to have
• Creative use of the logo in the slides. The Tirem icon may be used as a small device or large watermark to enhance branding.

```html
<!DOCTYPE html>
<html lang="en">
<head>
<meta charset="utf-8">
<title>Tirem – Presentation Master</title>
<link href="https://fonts.googleapis.com/css2?family=Poppins:ital,wght@1,600;1,700&family=Work+Sans:wght@400;500;600;700&display=swap" rel="stylesheet">
<style>
:root{
  --sky:#6ea6fa;--blue:#517ed8;--royal:#3758b4;--navy:#203390;--ink:#060d6c;--green:#2EC193;
  --grey:#a7a8ab;--line:#e3e5ea;--text:#222;--mute:#8a8f99;--slate:#3e4a66;
}
*{box-sizing:border-box;margin:0;padding:0}
html,body{width:1200px;height:1039px;overflow:hidden;background:var(--grey);font-family:"Work Sans",Arial,sans-serif;color:var(--text)}
.sheet{position:relative;width:1200px;height:1039px}
.slide{position:absolute;width:282px;height:159px;background:#fff;overflow:hidden;box-shadow:inset 0 -2px 0 #3b4a7a}
.slide::after{content:"";position:absolute;right:0;bottom:0;width:15px;height:12px;background:var(--sky);clip-path:polygon(100% 0,100% 100%,0 100%)}
.c1{left:17px}.c2{left:312px}.c3{left:606px}.c4{left:900px}
.r1{top:23px}.r2{top:190px}.r3{top:358px}.r4{top:525px}.r5{top:693px}.r6{top:861px}
.abs{position:absolute}
.mark{position:absolute;left:0;top:10px;width:26px;height:10px}
.title{position:absolute;left:28px;top:9px;font:italic 700 10.5px/1 "Poppins",sans-serif;color:#111;white-space:nowrap}
.title span{color:var(--sky)}
.lede{position:absolute;left:118px;top:11px;width:110px;font-size:3.4px;line-height:1.3;color:var(--mute)}
.brand{position:absolute;right:18px;top:12px;font:700 5px/1 "Work Sans",sans-serif;color:#111;letter-spacing:.2px;display:flex;align-items:center;gap:1.5px}
.brand i{width:4.5px;height:4.5px;border:1px solid #111;border-radius:50%}
.pg{position:absolute;right:19px;bottom:4px;font-size:3px;color:var(--mute)}
.photo{position:absolute}
.tiny{font-size:3.2px;line-height:1.35;color:var(--mute)}
.h{font-weight:600;color:#111}
.acc{color:var(--sky)}
.grn{color:var(--green)}
.tbl{position:absolute;border-collapse:collapse;font-size:2.6px;color:#333}
.tbl th{background:var(--sky);color:#fff;font-weight:500;padding:.8px 2px;text-align:left}
.tbl td{padding:.7px 2px;border-bottom:.3px solid var(--line)}
.tbl tr.sec td{background:#8c8f96;color:#fff;font-weight:600}
.social{position:absolute;display:flex;gap:1.5px}
.social i{width:4.5px;height:4.5px;background:var(--royal)}
</style>
</head>
<body>
<div class="sheet">

<section class="slide c1 r1">
  <svg class="abs" style="left:0;top:0" width="282" height="159" viewBox="0 0 282 159">
    <polygon points="0,159 0,112 88,0 160,0 40,159" fill="var(--navy)"/>
    <polygon points="0,159 0,146 96,30 102,30" fill="var(--green)"/>
    <line x1="30" y1="38" x2="61" y2="1" stroke="var(--sky)" stroke-width=".7"/>
    <polygon points="255,30 282,30 282,58 225,115 185,115" fill="var(--royal)"/>
    <polygon points="90,114 107,114 90,136 72,136" fill="var(--blue)"/>
  </svg>
  <div class="photo" role="img" aria-label="Racing yacht under sail on grey sea" style="left:43px;top:15px;width:205px;height:78px;clip-path:polygon(16% 0,100% 0,83% 100%,0 100%);background:linear-gradient(160deg,#c9ced6,#5f6873 55%,#2a2f38)"></div>
  <div class="brand" style="left:12px;right:auto;top:9px"><i></i>TIREM</div>
  <div class="abs" style="left:134px;top:117px;font:italic 700 9.5px/1 Poppins,sans-serif;color:#111">Welcome to our <span class="acc">race</span></div>
  <div class="abs" style="left:146px;top:131px;font-size:4.5px;color:#c3c6cc">Place the sub heading text here</div>
</section>

<section class="slide c2 r1">
  <svg class="mark" viewBox="0 0 26 10"><path d="M0 0h14L8 10H0z" fill="var(--ink)"/><path d="M17 0h4l-6 10h-4z" fill="var(--sky)"/></svg>
  <div class="title">Company <span>Intro</span></div>
  <div class="lede">Lorem ipsum dolor sit amet, consectetuer adipiscing elit. Maecenas porttitor congue massa.</div>
  <div class="brand"><i></i>TIREM</div>
  <div class="photo" role="img" aria-label="Two racing catamarans near a coastline" style="left:17px;top:40px;width:248px;height:100px;background:linear-gradient(180deg,#b9bfc9,#7d858f 60%,#4a525c)"></div>
  <div class="abs" style="left:17px;top:40px;width:120px;height:100px;background:rgba(32,51,144,.88);clip-path:polygon(0 0,100% 0,80% 100%,0 100%)"></div>
  <div class="abs" style="left:17px;top:40px;width:22px;height:20px;background:#e9ecf2;clip-path:polygon(0 0,100% 0,0 100%)"></div>
  <svg class="abs" style="left:36px;top:45px" width="8" height="7" viewBox="0 0 8 7"><path d="M1 0v7M1 1h6l-1.5 1.5L7 4H1" fill="none" stroke="#fff" stroke-width=".6"/></svg>
  <div class="abs" style="left:29px;top:85px;font-size:4.6px;font-weight:600;color:#fff;line-height:1.3">Layout with single<br>column and full <span class="acc">image</span></div>
  <div class="abs tiny" style="left:29px;top:98px;width:48px;color:#c8d2f0">Lorem ipsum is simply dummy text of the printing and typesetting industry</div>
  <div class="pg">2</div>
</section>

<section class="slide c3 r1">
  <svg class="mark" viewBox="0 0 26 10"><path d="M0 0h14L8 10H0z" fill="var(--ink)"/><path d="M17 0h4l-6 10h-4z" fill="var(--sky)"/></svg>
  <div class="title">Product <span>Image</span></div>
  <div class="lede">Lorem ipsum dolor sit amet, consectetuer adipiscing elit. Maecenas porttitor congue massa.</div>
  <div class="brand"><i></i>TIREM</div>
  <div class="photo" role="img" aria-label="Fleet of sailing yachts racing on deep blue water" style="left:13px;top:47px;width:161px;height:90px;background:linear-gradient(180deg,#9fb6cc,#2a5fa0 30%,#103a7a)"></div>
  <div class="abs" style="left:13px;top:47px;width:28px;height:26px;background:var(--sky);clip-path:polygon(0 0,100% 0,0 100%)"></div>
  <div class="abs" style="left:146px;top:110px;width:28px;height:27px;background:var(--green);clip-path:polygon(100% 0,100% 100%,0 100%)"></div>
  <div class="abs" style="left:182px;top:50px;font-size:5px;font-weight:600;line-height:1.2">The New Experience<br>of <span class="acc">Adventure</span></div>
  <div class="abs tiny" style="left:182px;top:66px;width:78px">Lorem ipsum has been the industry's standard dummy text ever since the 1500s, when an unknown printer took a galley of type and scrambled it to make a type specimen book.</div>
  <div class="abs tiny" style="left:182px;top:102px;line-height:1.8">Concept<br>Date<br>Cost<br>Partner<br>Services</div>
  <div class="abs tiny" style="left:201px;top:102px;line-height:1.8;color:#333">:&nbsp; Concept Name<br>:&nbsp; 25 Nov 22<br>:&nbsp; $133,000<br>:&nbsp; Corvane<br>:&nbsp; All In</div>
  <div class="pg">3</div>
</section>

<section class="slide c4 r1">
  <svg class="mark" viewBox="0 0 26 10"><path d="M0 0h14L8 10H0z" fill="var(--ink)"/><path d="M17 0h4l-6 10h-4z" fill="var(--sky)"/></svg>
  <div class="title">Video <span>Events</span></div>
  <div class="lede">Lorem ipsum dolor sit amet, consectetuer adipiscing elit. Maecenas porttitor congue massa.</div>
  <div class="brand"><i></i>TIREM</div>
  <div class="photo" role="img" aria-label="Harbour with moored yachts" style="left:17px;top:43px;width:67px;height:28px;background:linear-gradient(180deg,#b8c3cf,#6f8aa3)"></div>
  <div class="photo" role="img" aria-label="Crew working on deck" style="left:17px;top:75px;width:67px;height:28px;background:linear-gradient(180deg,#8d97a3,#5a626d)"></div>
  <div class="photo" role="img" aria-label="Boats racing near a coast" style="left:17px;top:107px;width:67px;height:28px;background:linear-gradient(180deg,#c4ccd4,#4f79a6)"></div>
  <div class="photo" role="img" aria-label="Aerial view of a yacht racing past a harbour" style="left:86px;top:43px;width:184px;height:93px;background:linear-gradient(150deg,#b6bcc3,#6a7580 50%,#3b4550)"></div>
  <div class="abs" style="left:210px;top:43px;width:60px;height:93px;background:rgba(6,13,108,.7)"></div>
  <svg class="abs" style="left:145px;top:80px" width="20" height="20" viewBox="0 0 20 20"><circle cx="10" cy="10" r="9" fill="none" stroke="#fff" stroke-width="1"/><path d="M8 6l6 4-6 4z" fill="#fff"/></svg>
  <div class="abs" style="left:215px;top:50px;font-size:4.3px;color:#fff;line-height:1.3">Lorem Ipsum is<br>simply dummy text</div>
  <div class="abs tiny" style="left:215px;top:64px;width:50px;color:#c7cde6">It has roots in a piece of classical Latin literature from 45 BC, making it over 2000 years old.</div>
  <div class="abs" style="left:215px;top:90px;width:47px;font-size:2.7px;color:#fff;line-height:1">
    <div style="border-bottom:1px solid var(--sky);padding-bottom:1.5px;margin-bottom:7px">Video Overview</div>
    <div style="border-bottom:1px solid var(--sky);padding-bottom:1.5px;margin-bottom:7px">Video Overview</div>
    <div style="border-bottom:1px solid var(--sky);padding-bottom:1.5px">Video Overview</div>
  </div>
</section>

<section class="slide c1 r2">
  <svg class="mark" viewBox="0 0 26 10"><path d="M0 0h14L8 10H0z" fill="var(--ink)"/><path d="M17 0h4l-6 10h-4z" fill="var(--sky)"/></svg>
  <div class="title">Company <span>Intro</span></div>
  <div class="lede">Lorem ipsum dolor sit amet, consectetuer adipiscing elit. Maecenas porttitor congue massa.</div>
  <div class="brand"><i></i>TIREM</div>
  <svg class="abs" style="left:0;top:0" width="282" height="159" viewBox="0 0 282 159" role="img" aria-label="Collage of sailing race photos in slanted frames">
    <polygon points="74,42 88,42 80,56 66,56" fill="var(--sky)"/>
    <polygon points="55,48 84,48 66,82 36,82" fill="#51606c"/>
    <polygon points="88,57 135,57 112,100 65,100" fill="#6f7f8c"/>
    <polygon points="125,68 150,68 140,84 115,84" fill="#c9ccd1"/>
    <polygon points="118,84 150,84 128,120 96,120" fill="#8aa9a0"/>
    <polygon points="66,100 86,100 76,118 56,118" fill="var(--green)"/>
    <polygon points="58,118 82,118 72,140 48,140" fill="#5a6670"/>
    <polygon points="96,122 116,122 108,134 88,134" fill="var(--blue)"/>
    <polygon points="128,118 146,118 140,130 122,130" fill="#e1e3e6"/>
  </svg>
  <div class="abs" style="left:175px;top:53px;font-size:5px;font-weight:600;line-height:1.2">The New Experience<br>of <span class="acc">Adventure</span></div>
  <div class="abs tiny" style="left:175px;top:68px;width:74px">Lorem ipsum has been the industry's standard dummy text ever since the 1500s, when an unknown printer took a galley of type and scrambled it to make a type specimen book.</div>
  <div class="abs" style="left:175px;top:101px;width:30px;height:8px;background:var(--navy);clip-path:polygon(0 0,100% 0,88% 100%,0 100%);font-size:2.8px;color:#fff;padding:2.4px 0 0 4px">Read More</div>
  <div class="pg">5</div>
</section>

<section class="slide c2 r2">
  <svg class="mark" viewBox="0 0 26 10"><path d="M0 0h14L8 10H0z" fill="var(--ink)"/><path d="M17 0h4l-6 10h-4z" fill="var(--sky)"/></svg>
  <div class="title">Our <span>Services</span></div>
  <div class="lede" style="width:125px">Lorem ipsum dolor sit amet, consectetuer adipiscing elit. Maecenas porttitor congue massa.</div>
  <div class="brand"><i></i>TIREM</div>
  <div class="photo" role="img" aria-label="Catamaran racing on blue-green water" style="left:0;top:26px;width:282px;height:126px;clip-path:polygon(0 10%,100% 0,100% 88%,35% 100%,0 100%);background:linear-gradient(160deg,var(--ink),var(--navy) 40%,#1b6f8a 80%,var(--green))"></div>
  <div class="abs" style="left:28px;top:75px;font-size:7.5px;color:#fff;line-height:1.15;width:95px">Lorem ipsum <span class="grn">dolor sit amet</span>, consectetuer adipiscing elit.</div>
  <div class="abs" style="left:142px;top:47px;display:grid;grid-template-columns:62px 62px;gap:3px">
    <div style="background:#fff;height:30px;padding:3px"><div style="font-size:4.5px;text-align:right">Our Services</div><div class="tiny" style="font-size:2.4px;margin-top:3px">Fusce posuere, magna sed pulvinar ultricies, purus lectus malesuada libero.</div></div>
    <div style="background:#fff;height:30px;padding:3px"><div style="font-size:4.5px;text-align:right">Our Services</div><div class="tiny" style="font-size:2.4px;margin-top:3px">Fusce posuere, magna sed pulvinar ultricies, purus lectus malesuada libero.</div></div>
    <div style="background:#fff;height:30px;padding:3px"><div style="font-size:4.5px;text-align:right">Our Services</div><div class="tiny" style="font-size:2.4px;margin-top:3px">Fusce posuere, magna sed pulvinar ultricies, purus lectus malesuada libero.</div></div>
    <div style="background:#fff;height:30px;padding:3px"><div style="font-size:4.5px;text-align:right">Our Services</div><div class="tiny" style="font-size:2.4px;margin-top:3px">Fusce posuere, magna sed pulvinar ultricies, purus lectus malesuada libero.</div></div>
  </div>
  <div class="pg">6</div>
</section>

<section class="slide c3 r2">
  <svg class="mark" viewBox="0 0 26 10"><path d="M0 0h14L8 10H0z" fill="var(--ink)"/><path d="M17 0h4l-6 10h-4z" fill="var(--sky)"/></svg>
  <div class="title">Our <span>Services</span></div>
  <div class="lede">Lorem ipsum dolor sit amet, consectetuer adipiscing elit. Maecenas porttitor congue massa.</div>
  <div class="brand"><i></i>TIREM</div>
  <svg class="abs" style="left:0;top:0" width="282" height="159" viewBox="0 0 282 159">
    <polygon points="32,46 142,46 128,69 20,69" fill="var(--sky)"/>
    <polygon points="145,46 260,46 246,69 133,69" fill="var(--navy)"/>
    <polygon points="28,76 138,76 124,99 16,99" fill="var(--blue)"/>
    <polygon points="141,76 256,76 242,99 129,99" fill="var(--ink)"/>
    <polygon points="24,105 134,105 120,128 12,128" fill="var(--royal)"/>
    <polygon points="137,105 252,105 238,128 125,128" fill="var(--green)"/>
    <g fill="#fff"><rect x="41" y="56" width="5" height="2"/><path d="M43.5 51l-3 3h6z"/></g>
    <path d="M155 53v6M155 53h6l-1 1.5 1 1.5h-6" fill="none" stroke="#fff" stroke-width=".6"/>
    <path d="M37 89a3 3 0 0 1 6 0zM40 89v3" fill="none" stroke="#fff" stroke-width=".6"/>
    <path d="M151 85h2l2-2v6l-2-2h-2z" fill="#fff"/>
    <rect x="33" y="113" width="4" height="5" fill="none" stroke="#fff" stroke-width=".6"/>
    <rect x="146" y="114" width="6" height="4.5" rx=".5" fill="#fff"/>
  </svg>
  <div class="abs" style="left:64px;top:48px;width:70px;color:#fff"><div style="font-size:4.5px">Our Services</div><div style="font-size:2.2px;opacity:.8">Fusce posuere, magna sed pulvinar ultricies, purus lectus malesuada libero sit amet.</div></div>
  <div class="abs" style="left:177px;top:48px;width:70px;color:#fff"><div style="font-size:4.5px">Our Services</div><div style="font-size:2.2px;opacity:.8">Fusce posuere, magna sed pulvinar ultricies, purus lectus malesuada libero sit amet.</div></div>
  <div class="abs" style="left:60px;top:78px;width:70px;color:#fff"><div style="font-size:4.5px">Our Services</div><div style="font-size:2.2px;opacity:.8">Fusce posuere, magna sed pulvinar ultricies, purus lectus malesuada libero sit amet.</div></div>
  <div class="abs" style="left:173px;top:78px;width:70px;color:#fff"><div style="font-size:4.5px">Our Services</div><div style="font-size:2.2px;opacity:.8">Fusce posuere, magna sed pulvinar ultricies, purus lectus malesuada libero sit amet.</div></div>
  <div class="abs" style="left:56px;top:107px;width:70px;color:#fff"><div style="font-size:4.5px">Our Services</div><div style="font-size:2.2px;opacity:.8">Fusce posuere, magna sed pulvinar ultricies, purus lectus malesuada libero sit amet.</div></div>
  <div class="abs" style="left:169px;top:107px;width:70px;color:#fff"><div style="font-size:4.5px">Our Services</div><div style="font-size:2.2px;opacity:.8">Fusce posuere, magna sed pulvinar ultricies, purus lectus malesuada libero sit amet.</div></div>
  <div class="pg">7</div>
</section>

<section class="slide c4 r2">
  <svg class="mark" viewBox="0 0 26 10"><path d="M0 0h14L8 10H0z" fill="var(--ink)"/><path d="M17 0h4l-6 10h-4z" fill="var(--sky)"/></svg>
  <div class="title">Our <span>Project</span></div>
  <div class="lede">Lorem ipsum dolor sit amet, consectetuer adipiscing elit. Maecenas porttitor congue massa.</div>
  <div class="brand"><i></i>TIREM</div>
  <svg class="abs" style="left:0;top:0" width="282" height="159" viewBox="0 0 282 159" role="img" aria-label="Five slanted photos of project race yachts">
    <g><polygon points="47,46 85,46 63,85 25,85" fill="#7d8a96"/><polygon points="91,46 129,46 107,85 69,85" fill="#3f73a6"/><polygon points="135,46 173,46 151,85 113,85" fill="#5e86ad"/><polygon points="179,46 217,46 195,85 157,85" fill="#8b9aa0"/><polygon points="223,46 261,46 239,85 201,85" fill="#3e6e9a"/></g>
    <g font-size="4" fill="#333" font-family="Work Sans"><text x="33" y="82">01</text><text x="77" y="82">02</text><text x="121" y="82">03</text><text x="165" y="82">04</text><text x="209" y="82">05</text></g>
  </svg>
  <div class="abs" style="left:21px;top:100px;display:flex;gap:8px">
    <div style="width:36px"><div class="h" style="font-size:3.8px;line-height:1.2">Your subtitle<br>here</div><div class="tiny" style="font-size:2.7px;margin-top:3px">Lorem ipsum is simply dummy text of the printing and typesetting industry.</div></div>
    <div style="width:36px"><div class="h" style="font-size:3.8px;line-height:1.2">Your subtitle<br>here</div><div class="tiny" style="font-size:2.7px;margin-top:3px">Lorem ipsum is simply dummy text of the printing and typesetting industry.</div></div>
    <div style="width:36px"><div class="h" style="font-size:3.8px;line-height:1.2">Your subtitle<br>here</div><div class="tiny" style="font-size:2.7px;margin-top:3px">Lorem ipsum is simply dummy text of the printing and typesetting industry.</div></div>
    <div style="width:36px"><div class="h" style="font-size:3.8px;line-height:1.2">Your subtitle<br>here</div><div class="tiny" style="font-size:2.7px;margin-top:3px">Lorem ipsum is simply dummy text of the printing and typesetting industry.</div></div>
    <div style="width:36px"><div class="h" style="font-size:3.8px;line-height:1.2">Your subtitle<br>here</div><div class="tiny" style="font-size:2.7px;margin-top:3px">Lorem ipsum is simply dummy text of the printing and typesetting industry.</div></div>
  </div>
  <div class="pg">8</div>
</section>

<section class="slide c1 r3">
  <svg class="mark" viewBox="0 0 26 10"><path d="M0 0h14L8 10H0z" fill="var(--ink)"/><path d="M17 0h4l-6 10h-4z" fill="var(--sky)"/></svg>
  <div class="title">Our <span>Timeline</span></div>
  <div class="lede">Lorem ipsum dolor sit amet, consectetuer adipiscing elit. Maecenas porttitor congue massa.</div>
  <div class="brand"><i></i>TIREM</div>
  <svg class="abs" style="left:0;top:0" width="282" height="159" viewBox="0 0 282 159">
    <rect x="0" y="54" width="255" height="5" fill="var(--sky)"/><polygon points="150,54 255,54 252,59 147,59" fill="var(--navy)"/>
    <g stroke="var(--sky)" stroke-width=".6"><line x1="90" y1="59" x2="90" y2="82"/><line x1="126" y1="59" x2="126" y2="109"/><line x1="174" y1="59" x2="174" y2="77"/><line x1="227" y1="59" x2="227" y2="134"/></g>
    <g fill="var(--royal)"><circle cx="90" cy="88" r="9"/><circle cx="126" cy="114" r="9"/><circle cx="174" cy="83" r="9"/><circle cx="227" cy="141" r="9"/></g>
    <g fill="#fff" font-size="3.6" text-anchor="middle" font-family="Work Sans"><text x="90" y="93">2015</text><text x="126" y="119">2017</text><text x="174" y="88">2020</text><text x="227" y="146">2022</text></g>
  </svg>
  <div class="abs" style="left:30px;top:80px;width:48px;text-align:right"><div class="h" style="font-size:4px">Your subtitle here</div><div class="tiny" style="font-size:2.7px;margin-top:1px">Lorem ipsum is simply dummy text of the printing and typesetting industry.</div></div>
  <div class="abs" style="left:141px;top:103px;width:48px"><div class="h" style="font-size:4px">Your subtitle here</div><div class="tiny" style="font-size:2.7px;margin-top:1px">Lorem ipsum is simply dummy text of the printing and typesetting industry.</div></div>
  <div class="abs" style="left:190px;top:74px;width:48px"><div class="h" style="font-size:4px">Your subtitle here</div><div class="tiny" style="font-size:2.7px;margin-top:1px">Lorem ipsum is simply dummy text of the printing and typesetting industry.</div></div>
  <div class="abs" style="left:165px;top:128px;width:48px;text-align:right"><div class="h" style="font-size:4px">Your subtitle here</div><div class="tiny" style="font-size:2.7px;margin-top:1px">Lorem ipsum is simply dummy text of the printing and typesetting industry.</div></div>
  <div class="pg">9</div>
</section>

<section class="slide c2 r3">
  <svg class="mark" viewBox="0 0 26 10"><path d="M0 0h14L8 10H0z" fill="var(--ink)"/><path d="M17 0h4l-6 10h-4z" fill="var(--sky)"/></svg>
  <div class="title">Our <span>Milestone</span></div>
  <div class="lede">Lorem ipsum dolor sit amet, consectetuer adipiscing elit. Maecenas porttitor congue massa.</div>
  <div class="brand"><i></i>TIREM</div>
  <svg class="abs" style="left:0;top:0" width="282" height="159" viewBox="0 0 282 159">
    <line x1="15" y1="130" x2="262" y2="130" stroke="var(--royal)" stroke-width=".5" stroke-dasharray="1.2 1"/>
    <g stroke-width="1.4"><line x1="54" y1="86" x2="54" y2="130" stroke="var(--sky)"/><line x1="96" y1="65" x2="96" y2="130" stroke="var(--blue)"/><line x1="137" y1="86" x2="137" y2="130" stroke="var(--royal)"/><line x1="179" y1="65" x2="179" y2="130" stroke="var(--ink)"/><line x1="221" y1="86" x2="221" y2="130" stroke="var(--green)"/></g>
    <circle cx="54" cy="84" r="12" fill="var(--sky)"/><circle cx="96" cy="63" r="12" fill="var(--blue)"/><circle cx="137" cy="84" r="12" fill="var(--royal)"/><circle cx="179" cy="63" r="12" fill="var(--ink)"/><circle cx="221" cy="84" r="12" fill="var(--green)"/>
    <g fill="#fff" font-size="4" text-anchor="middle" font-family="Work Sans" font-weight="600"><text x="54" y="85.5">2015</text><text x="96" y="64.5">2017</text><text x="137" y="85.5">2019</text><text x="179" y="64.5">2021</text><text x="221" y="85.5">2023</text></g>
    <g stroke-width=".8" fill="#fff"><circle cx="54" cy="130" r="2" stroke="var(--sky)"/><circle cx="96" cy="130" r="2" stroke="var(--blue)"/><circle cx="137" cy="130" r="2" stroke="var(--royal)"/><circle cx="179" cy="130" r="2" stroke="var(--ink)"/><circle cx="221" cy="130" r="2" stroke="var(--green)"/></g>
    <g fill="#666" font-size="3.5" font-family="Work Sans"><text x="59" y="107">Write your</text><text x="59" y="112">paragraph</text><text x="59" y="117">here</text><text x="101" y="107">Write your</text><text x="101" y="112">paragraph</text><text x="101" y="117">here</text><text x="142" y="107">Write your</text><text x="142" y="112">paragraph</text><text x="142" y="117">here</text><text x="184" y="107">Write your</text><text x="184" y="112">paragraph</text><text x="184" y="117">here</text><text x="226" y="107">Write your</text><text x="226" y="112">paragraph</text><text x="226" y="117">here</text></g>
  </svg>
  <div class="pg">10</div>
</section>

<section class="slide c3 r3" style="box-shadow:none">
  <div class="photo" role="img" aria-label="Dark blue-green sea with racing yacht" style="left:0;top:0;width:282px;height:159px;background:linear-gradient(160deg,#1f5c5a,#143a62 45%,var(--ink))"></div>
  <div class="abs" style="left:0;top:0;width:282px;height:159px;background:rgba(6,13,108,.45)"></div>
  <div class="title" style="left:22px;color:#fff">Table <span>Layout</span></div>
  <div class="lede" style="left:131px;color:#c7d0e8">Lorem ipsum dolor sit amet, consectetuer adipiscing elit. Maecenas porttitor congue massa.</div>
  <svg class="abs" style="left:0;top:0" width="282" height="159" viewBox="0 0 282 159">
    <rect x="110" y="49" width="39" height="8" fill="var(--sky)"/><rect x="149" y="49" width="39" height="8" fill="var(--blue)"/><rect x="188" y="49" width="39" height="8" fill="var(--royal)"/><rect x="227" y="49" width="39" height="8" fill="var(--green)"/>
    <g fill="#fff" font-size="4" text-anchor="middle" font-family="Work Sans"><text x="129" y="54.5">Label 1</text><text x="168" y="54.5">Label 2</text><text x="207" y="54.5">Label 3</text><text x="246" y="54.5">Label 4</text></g>
    <g stroke="rgba(255,255,255,.3)" stroke-width=".3"><line x1="22" y1="64" x2="266" y2="64"/><line x1="22" y1="74" x2="266" y2="74"/><line x1="22" y1="83.5" x2="266" y2="83.5"/><line x1="22" y1="93" x2="266" y2="93"/><line x1="22" y1="103" x2="266" y2="103"/><line x1="22" y1="112.5" x2="266" y2="112.5"/><line x1="22" y1="122" x2="266" y2="122"/><line x1="22" y1="132" x2="266" y2="132"/></g>
    <g fill="#dfe4f3" font-size="3.2" font-family="Work Sans"><text x="24" y="62">Lorem Ipsum is simply dummy text</text><text x="24" y="72">It has roots in a piece of.</text><text x="24" y="81.5">Lorem Ipsum is not simply random text.</text><text x="24" y="91">Lorem Ipsum is simply dummy text</text><text x="24" y="101">It has roots in a piece of.</text><text x="24" y="110.5">Lorem Ipsum is not simply random text.</text><text x="24" y="120">Lorem Ipsum is simply dummy text</text><text x="24" y="130">It has roots in a piece of.</text></g>
    <g fill="var(--green)"><circle cx="129" cy="61" r=".8"/><circle cx="168" cy="61" r=".8"/><circle cx="246" cy="61" r=".8"/><circle cx="207" cy="71" r=".8"/><circle cx="129" cy="90" r=".8"/><circle cx="168" cy="90" r=".8"/><circle cx="246" cy="90" r=".8"/><circle cx="129" cy="100" r=".8"/><circle cx="246" cy="100" r=".8"/><circle cx="246" cy="110" r=".8"/><circle cx="168" cy="119" r=".8"/><circle cx="207" cy="119" r=".8"/><circle cx="168" cy="129" r=".8"/><circle cx="207" cy="129" r=".8"/><circle cx="168" cy="80" r=".8"/><circle cx="129" cy="80" r=".8"/></g>
    <g stroke="#fff" stroke-width=".4"><path d="M166.5 59.5l3 3M169.5 59.5l-3 3"/><path d="M205.5 59.5l3 3M208.5 59.5l-3 3"/><path d="M127.5 69.5l3 3M130.5 69.5l-3 3"/><path d="M166.5 69.5l3 3M169.5 69.5l-3 3"/><path d="M244.5 69.5l3 3M247.5 69.5l-3 3"/><path d="M205.5 78.5l3 3M208.5 78.5l-3 3"/><path d="M244.5 78.5l3 3M247.5 78.5l-3 3"/><path d="M205.5 88.5l3 3M208.5 88.5l-3 3"/><path d="M166.5 98.5l3 3M169.5 98.5l-3 3"/><path d="M205.5 98.5l3 3M208.5 98.5l-3 3"/><path d="M127.5 108.5l3 3M130.5 108.5l-3 3"/><path d="M166.5 108.5l3 3M169.5 108.5l-3 3"/><path d="M205.5 108.5l3 3M208.5 108.5l-3 3"/><path d="M127.5 117.5l3 3M130.5 117.5l-3 3"/><path d="M244.5 117.5l3 3M247.5 117.5l-3 3"/><path d="M127.5 127.5l3 3M130.5 127.5l-3 3"/><path d="M244.5 127.5l3 3M247.5 127.5l-3 3"/></g>
    <g fill="#fff" font-size="3.5" text-anchor="middle" font-family="Work Sans"><text x="129" y="140">$ 99,99</text><text x="168" y="140">$ 99,99</text><text x="207" y="140">$ 99,99</text><text x="246" y="140">$ 99,99</text></g>
  </svg>
</section>

<section class="slide c4 r3">
  <svg class="mark" viewBox="0 0 26 10"><path d="M0 0h14L8 10H0z" fill="var(--ink)"/><path d="M17 0h4l-6 10h-4z" fill="var(--sky)"/></svg>
  <div class="title">Annual <span>Table</span></div>
  <div class="lede">Lorem ipsum dolor sit amet, consectetuer adipiscing elit. Maecenas porttitor congue massa.</div>
  <div class="brand"><i></i>TIREM</div>
  <svg class="abs" style="left:19px;top:41px" width="48" height="22" viewBox="0 0 48 22"><circle cx="11" cy="11" r="10" fill="none" stroke="#111" stroke-width=".8"/><path d="M6 6l10 10M16 6L6 16" stroke="#111" stroke-width=".8"/><circle cx="36" cy="11" r="10" fill="none" stroke="#111" stroke-width=".8"/><path d="M36 5v12M33 6h6" stroke="#111" stroke-width=".8"/></svg>
  <div class="abs" style="left:85px;top:42px;font-size:4.5px;font-weight:600">Company budget files 2021</div>
  <div class="abs tiny" style="left:85px;top:49px;width:134px;font-size:2.4px;font-style:italic">Lorem ipsum dolor sit amet, ligula suspendisse nulla pretium, rhoncus tempor fermentum, enim integer ad vestibulum volutpat. Nisl rhoncus turpis est, vel elit, congue wisi enim nunc ultricies sit, magna tincidunt.</div>
  <table class="tbl" style="left:20px;top:63px;width:200px;font-size:3px">
    <tr style="color:var(--blue)"><td style="width:64px">Nisl rhoncus turpis est</td><td>2014</td><td>2015</td><td>2016</td><td>2017</td></tr>
    <tr style="color:#999"><td>Praesent condimentum arcu</td><td>4,456</td><td>4,456</td><td>4,456</td><td>4,456</td></tr>
    <tr style="color:#999"><td>Praesent condimentum arcu</td><td>5,345</td><td>5,345</td><td>5,345</td><td>5,345</td></tr>
    <tr style="color:#999"><td>Praesent condimentum arcu</td><td>6,567</td><td>6,567</td><td>6,567</td><td>6,567</td></tr>
    <tr style="color:#999"><td>Praesent condimentum arcu</td><td>7,678</td><td>7,678</td><td>7,678</td><td>7,678</td></tr>
    <tr style="color:#999"><td>Praesent condimentum arcu</td><td>8,789</td><td>8,789</td><td>8,789</td><td>8,789</td></tr>
    <tr><td style="border:0">CHANGE 20%</td><td colspan="4" style="border:0"></td></tr>
  </table>
  <div class="abs" style="left:221px;top:41px;width:61px;height:15px;background:#4a5160;color:#fff;font-size:3.3px;padding:5.5px 0 0 7px">STATS MANAGER</div>
  <div class="abs" style="left:221px;top:56px;width:61px;height:91px;background:var(--blue);color:#fff;font-size:3.5px;padding:6px 0 0 7px;line-height:1.3">
    <div style="color:#d8e4ff">THIS YEAR</div><div style="margin-bottom:10px">17,250</div>
    <div style="color:#d8e4ff">THIS MONTH</div><div style="margin-bottom:10px">3,000</div>
    <div style="color:#d8e4ff">THIS WEEK</div><div style="margin-bottom:10px">450</div>
    <div style="color:#d8e4ff">TODAY</div><div>225</div>
  </div>
</section>

<section class="slide c1 r4">
  <svg class="mark" viewBox="0 0 26 10"><path d="M0 0h14L8 10H0z" fill="var(--ink)"/><path d="M17 0h4l-6 10h-4z" fill="var(--sky)"/></svg>
  <div class="title">Race <span>Calendar</span></div>
  <div class="lede">Lorem ipsum dolor sit amet, consectetuer adipiscing elit. Maecenas porttitor congue massa.</div>
  <div class="brand"><i></i>TIREM</div>
  <table class="tbl" style="left:10px;top:33px;width:261px">
    <tr><th style="background:#fff;color:#111;width:88px">EVENTS</th><th>LOCATION</th><th>START</th><th>DURÉE-EVENTS</th><th>DISTANCE</th></tr>
    <tr class="sec"><td colspan="5">Spring – North East USA</td></tr>
    <tr><td>Harbour Light Race</td><td>Newport</td><td>Juin</td><td>10j</td><td>635</td></tr>
    <tr class="sec"><td colspan="5">Spring – Summer – Northern Europe</td></tr>
    <tr><td>Isle Circuit</td><td>Belle Ile</td><td>Mai</td><td>3j</td><td></td></tr>
    <tr><td>Westwind Race</td><td>La Trinité sur Mer</td><td>Mai</td><td>4j</td><td></td></tr>
    <tr><td>Cross Channel Sprint</td><td>La Trinité – Cowes</td><td>Juillet</td><td>7j</td><td>350</td></tr>
    <tr><td>Coastline Dash</td><td>Cowes dinard</td><td>Juillet</td><td>3j</td><td>151</td></tr>
    <tr><td>Channel Cup</td><td>Cherbourg – La Trinité</td><td>Juillet</td><td>6j</td><td></td></tr>
    <tr><td>Northern Sea Race</td><td>Helsinki</td><td>Juillet</td><td>9j</td><td>635</td></tr>
    <tr><td>Corvane Rock Race</td><td>Cowes – cherbourg</td><td>Juillet</td><td>6j</td><td>695</td></tr>
    <tr><td>Solent Week</td><td>Cowes</td><td>Juillet</td><td>8j</td><td>Coastal</td></tr>
    <tr><td>Round the Isles Race</td><td>Cowes</td><td>Août</td><td>9j</td><td></td></tr>
    <tr><td>Multihull Trophy</td><td>La Trinité sur mer</td><td>Août</td><td>4j</td><td>Coastal</td></tr>
  </table>
  <div class="pg">13</div>
</section>

<section class="slide c2 r4">
  <svg class="mark" viewBox="0 0 26 10"><path d="M0 0h14L8 10H0z" fill="var(--ink)"/><path d="M17 0h4l-6 10h-4z" fill="var(--sky)"/></svg>
  <div class="title">Race <span>Calendar</span></div>
  <div class="lede">Lorem ipsum dolor sit amet, consectetuer adipiscing elit. Maecenas porttitor congue massa.</div>
  <div class="brand"><i></i>TIREM</div>
  <table class="tbl" style="left:9px;top:33px;width:264px;font-size:2.4px">
    <tr><th style="background:#fff;color:#111;width:88px">EVENTS</th><th>LOCATION</th><th>START</th><th>DURÉE-EVENTS</th><th>DISTANCE</th></tr>
    <tr class="sec"><td colspan="5">Summer Europe – Méditerranéen</td></tr>
    <tr><td>Twin Hull Series</td><td>Mallorca – Port Adriano</td><td>Août</td><td>5j</td><td>3x30nm</td></tr>
    <tr><td>Corvane Island Race</td><td>Valletta – Malta</td><td>Octobre</td><td>10j</td><td>606</td></tr>
    <tr class="sec"><td colspan="5">Transats</td></tr>
    <tr><td>Trade Wind Crossing</td><td>Lanzarote – Grenada</td><td>Janvier</td><td>6+5j</td><td>2995</td></tr>
    <tr><td>Blue Water Rally</td><td>Canaries – St Lucia</td><td>Novembre</td><td></td><td>2700</td></tr>
    <tr><td>North Atlantic Dash</td><td>Québec – St Malo</td><td>Juillet 2024</td><td>3+10j</td><td>3000</td></tr>
    <tr><td>Spice Route Solo</td><td>St Malo – Guadeloupe</td><td>Novembre 2022</td><td>2+18j</td><td>3000</td></tr>
    <tr class="sec"><td colspan="5">Winter – Spring – Caribbean</td></tr>
    <tr><td>Island Multihull Challenge</td><td>St Maarten</td><td>Février</td><td>3j</td><td>Coastal</td></tr>
    <tr><td>Leeward 600</td><td>Antigua</td><td>Février</td><td>8j</td><td>600</td></tr>
    <tr><td>Lagoon Spring Regatta</td><td>St Maarten</td><td>Mars</td><td>7j</td><td>Coastal</td></tr>
    <tr><td>Coral Bay Regatta</td><td>St Thomas – BVI</td><td>Mars</td><td>5j</td><td>Coastal</td></tr>
    <tr><td>Reef Spring Regatta</td><td>BVI</td><td>Mars</td><td>7j</td><td>Coastal</td></tr>
    <tr><td>Trade Sails Week</td><td>St Barthelemy</td><td>Avril</td><td>7j</td><td>Coastal</td></tr>
    <tr><td>Windward Sailing Week</td><td>Antigua</td><td>Avril</td><td>8j</td><td>Coastal</td></tr>
  </table>
  <div class="pg">14</div>
</section>

<section class="slide c3 r4">
  <svg class="mark" viewBox="0 0 26 10"><path d="M0 0h14L8 10H0z" fill="var(--ink)"/><path d="M17 0h4l-6 10h-4z" fill="var(--sky)"/></svg>
  <div class="title">Calendar <span>Table</span></div>
  <div class="lede">Lorem ipsum dolor sit amet, consectetuer adipiscing elit. Maecenas porttitor congue massa.</div>
  <div class="brand"><i></i>TIREM</div>
  <svg class="abs" style="left:0;top:0" width="282" height="159" viewBox="0 0 282 159">
    <rect x="17" y="36" width="248" height="7" fill="#4c5568"/><rect x="17" y="43" width="248" height="6" fill="#dde0e6"/><rect x="17" y="49" width="248" height="46" fill="#f1f2f4"/>
    <text x="141" y="41.3" fill="#fff" font-size="4.2" text-anchor="middle" font-family="Work Sans">July</text>
    <g fill="#555" font-size="3" text-anchor="middle" font-family="Work Sans"><text x="35" y="47.2">Sun</text><text x="70" y="47.2">Mon</text><text x="106" y="47.2">Tue</text><text x="141" y="47.2">Wed</text><text x="176" y="47.2">Thu</text><text x="212" y="47.2">Fri</text><text x="247" y="47.2">Sat</text></g>
    <rect x="88" y="57" width="35" height="7" fill="var(--blue)"/><rect x="230" y="57" width="35" height="7" fill="var(--ink)"/><rect x="123" y="86" width="36" height="8" fill="var(--green)"/>
    <g fill="#555" font-size="3" text-anchor="middle" font-family="Work Sans"><text x="141" y="55">2</text><text x="176" y="55">3</text><text x="212" y="55">4</text><text x="247" y="55">5</text>
      <text x="35" y="62">6</text><text x="70" y="62">7</text><text x="106" y="62" fill="#fff">8</text><text x="141" y="62">9</text><text x="176" y="62">10</text><text x="212" y="62">11</text><text x="247" y="62" fill="#fff">12</text>
      <text x="35" y="71">13</text><text x="70" y="71">14</text><text x="106" y="71">15</text><text x="141" y="71">16</text><text x="176" y="71">17</text><text x="212" y="71">18</text><text x="247" y="71">19</text>
      <text x="35" y="80">20</text><text x="70" y="80">21</text><text x="106" y="80">22</text><text x="141" y="80">23</text><text x="176" y="80">24</text><text x="212" y="80">25</text><text x="247" y="80">26</text>
      <text x="35" y="90">27</text><text x="70" y="90">28</text><text x="106" y="90">29</text><text x="141" y="90" fill="#fff">30</text><text x="176" y="90">31</text></g>
    <circle cx="26" cy="118" r="7" fill="var(--blue)"/><circle cx="110" cy="118" r="7" fill="var(--green)"/><circle cx="192" cy="118" r="7" fill="var(--ink)"/>
    <g fill="none" stroke="#fff" stroke-width=".6"><circle cx="26" cy="118" r="3"/><rect x="108" y="115" width="4" height="6"/><circle cx="192" cy="118" r="3.5"/><path d="M188.5 118h7M192 114.5v7"/></g>
  </svg>
  <div class="abs" style="left:40px;top:111px;width:60px"><div class="h" style="font-size:3.8px">Knowledge</div><div class="tiny" style="font-size:2.7px;margin-top:2px">To get your company's name out there, you need to make sure.</div></div>
  <div class="abs" style="left:123px;top:111px;width:60px"><div class="h" style="font-size:3.8px">Awareness</div><div class="tiny" style="font-size:2.7px;margin-top:2px">To get your company's name out there, you need to make sure.</div></div>
  <div class="abs" style="left:205px;top:111px;width:60px"><div class="h" style="font-size:3.8px">Reinforcement</div><div class="tiny" style="font-size:2.7px;margin-top:2px">To get your company's name out there, you need to make sure.</div></div>
  <div class="pg">15</div>
</section>

<section class="slide c4 r4">
  <svg class="mark" viewBox="0 0 26 10"><path d="M0 0h14L8 10H0z" fill="var(--ink)"/><path d="M17 0h4l-6 10h-4z" fill="var(--sky)"/></svg>
  <div class="title">Product <span>Image</span></div>
  <div class="lede">Lorem ipsum dolor sit amet, consectetuer adipiscing elit. Maecenas porttitor congue massa.</div>
  <div class="brand"><i></i>TIREM</div>
  <div class="abs" style="left:24px;top:40px;width:54px;height:101px;background:#f2f3f5">
    <div class="photo" role="img" aria-label="Racing yacht sail close-up" style="left:0;top:0;width:54px;height:45px;background:linear-gradient(180deg,#c6ccd4,#525b66)"></div>
    <div class="abs" style="left:-4px;top:41px;width:34px;height:8px;background:var(--navy);clip-path:polygon(10% 0,100% 0,88% 100%,0 100%);color:#fff;font-size:4px;padding:1.5px 0 0 7px">SKU01</div>
    <div class="abs" style="left:0;top:50px;width:13px;height:5px;background:var(--navy);color:#fff;font-size:3px;padding:.8px 0 0 3px">$10.5</div>
    <div class="abs" style="left:5px;top:63px;width:46px"><div class="h" style="font-size:3.7px">Product Description</div><div class="tiny" style="font-size:2.7px;margin-top:2px">Lorem ipsum is simply dummy text of the printing and typesetting industry.</div></div>
  </div>
  <div class="abs" style="left:97px;top:40px;width:54px;height:101px;background:#f2f3f5">
    <div class="photo" role="img" aria-label="Yacht with green hull heeling" style="left:0;top:0;width:54px;height:45px;background:linear-gradient(180deg,#c6ccd4,#5a6670)"></div>
    <div class="abs" style="left:-4px;top:41px;width:34px;height:8px;background:var(--blue);clip-path:polygon(10% 0,100% 0,88% 100%,0 100%);color:#fff;font-size:4px;padding:1.5px 0 0 7px">SKU02</div>
    <div class="abs" style="left:0;top:50px;width:13px;height:5px;background:var(--blue);color:#fff;font-size:3px;padding:.8px 0 0 3px">$10.5</div>
    <div class="abs" style="left:5px;top:63px;width:46px"><div class="h" style="font-size:3.7px">Product Description</div><div class="tiny" style="font-size:2.7px;margin-top:2px">Lorem ipsum is simply dummy text of the printing and typesetting industry.</div></div>
  </div>
  <div class="abs" style="left:170px;top:40px;width:54px;height:101px;background:#f2f3f5">
    <div class="photo" role="img" aria-label="Catamaran racing at speed" style="left:0;top:0;width:54px;height:45px;background:linear-gradient(180deg,#c6ccd4,#4e5a63)"></div>
    <div class="abs" style="left:-4px;top:41px;width:34px;height:8px;background:var(--green);clip-path:polygon(10% 0,100% 0,88% 100%,0 100%);color:#fff;font-size:4px;padding:1.5px 0 0 7px">SKU03</div>
    <div class="abs" style="left:0;top:50px;width:13px;height:5px;background:var(--green);color:#fff;font-size:3px;padding:.8px 0 0 3px">$10.5</div>
    <div class="abs" style="left:5px;top:63px;width:46px"><div class="h" style="font-size:3.7px">Product Description</div><div class="tiny" style="font-size:2.7px;margin-top:2px">Lorem ipsum is simply dummy text of the printing and typesetting industry.</div></div>
  </div>
  <div class="pg">16</div>
</section>

<section class="slide c1 r5">
  <svg class="mark" viewBox="0 0 26 10"><path d="M0 0h14L8 10H0z" fill="var(--ink)"/><path d="M17 0h4l-6 10h-4z" fill="var(--sky)"/></svg>
  <div class="title">Product <span>Image</span></div>
  <div class="lede">Lorem ipsum dolor sit amet, consectetuer adipiscing elit. Maecenas porttitor congue massa.</div>
  <div class="brand"><i></i>TIREM</div>
  <div class="abs" style="left:25px;top:43px;width:62px;height:91px;background:var(--slate);padding:7px 7px;color:#fff">
    <div style="font-size:4.3px;line-height:1.25">Lorem Ipsum is<br>simply dummy text</div>
    <div style="font-size:2.7px;line-height:1.35;color:#c5ccdb;margin-top:4px">It has roots in a piece of classical Latin literature from 45 BC, making it over 2000 years old.</div>
    <div style="font-size:2.7px;margin-top:6px;border-bottom:1px solid var(--sky);padding-bottom:1.5px">Product Features</div>
    <div style="font-size:2.7px;margin-top:6px;border-bottom:1px solid var(--sky);padding-bottom:1.5px">Product Features</div>
    <div style="font-size:2.7px;margin-top:6px;border-bottom:1px solid var(--sky);padding-bottom:1.5px">Product Features</div>
  </div>
  <div class="abs" style="left:75px;top:120px;width:12px;height:14px;background:var(--sky);clip-path:polygon(100% 0,100% 100%,0 100%)"></div>
  <div class="abs" style="left:92px;top:43px;width:42px;height:8px;background:var(--navy);clip-path:polygon(0 0,100% 0,85% 100%,0 100%);color:#fff;font-size:4.3px;padding:1.5px 0 0 5px">SKU01</div>
  <div class="abs" style="left:92px;top:53px;width:22px;height:6px;background:var(--navy);clip-path:polygon(0 0,100% 0,80% 100%,0 100%);color:#fff;font-size:3.3px;padding:1px 0 0 4px">$10.5</div>
  <div class="photo" role="img" aria-label="Technical side and deck plan drawing of a racing yacht" style="left:138px;top:47px;width:120px;height:90px;background:linear-gradient(180deg,#f7f8fa,#eceef2)"></div>
  <div class="pg">17</div>
</section>

<section class="slide c2 r5">
  <svg class="abs" style="left:0;top:0" width="282" height="159" viewBox="0 0 282 159">
    <circle cx="70" cy="70" r="40" fill="none" stroke="#f2f3f5" stroke-width="3"/>
    <polygon points="195,0 282,0 282,159 84,159" fill="var(--navy)"/>
  </svg>
  <div class="brand" style="color:#fff;top:11px"><i style="border-color:#fff"></i>TIREM</div>
  <div class="photo" role="img" aria-label="Yacht with bright green hull racing on dark sea" style="left:188px;top:26px;width:94px;height:104px;background:linear-gradient(160deg,#3d5566,#1f3140 60%,#7dc24a 90%);clip-path:polygon(35% 0,100% 0,100% 100%,0 100%)"></div>
  <div class="abs" style="left:135px;top:103px;width:55px;height:18px;background:var(--royal);clip-path:polygon(20% 0,100% 0,82% 100%,0 100%);color:#fff;font-size:4.2px;padding:6px 0 0 11px">10.00 – 10.15</div>
  <div class="abs" style="left:23px;top:62px;font:italic 700 10px/1 Poppins,sans-serif;color:#111">Section <span class="acc">Break</span></div>
  <div class="abs" style="left:23px;top:77px;font-size:4.5px;color:#666">Place the sub heading text here</div>
  <div class="social" style="left:247px;top:141px"><i></i><i></i><i></i><i></i></div>
</section>

<section class="slide c3 r5">
  <svg class="mark" viewBox="0 0 26 10"><path d="M0 0h14L8 10H0z" fill="var(--ink)"/><path d="M17 0h4l-6 10h-4z" fill="var(--sky)"/></svg>
  <div class="title">Graph <span>Chart</span></div>
  <div class="lede">Lorem ipsum dolor sit amet, consectetuer adipiscing elit. Maecenas porttitor congue massa.</div>
  <div class="brand"><i></i>TIREM</div>
  <svg class="abs" style="left:0;top:0" width="282" height="159" viewBox="0 0 282 159">
    <g fill="#c9cbcf"><rect x="32" y="85" width="9" height="24"/><rect x="50" y="96" width="9" height="13"/><rect x="68" y="86" width="9" height="23"/><rect x="86" y="84" width="9" height="25"/><rect x="104" y="90" width="9" height="19"/><rect x="122" y="74" width="9" height="35"/><rect x="140" y="69" width="9" height="40"/></g>
    <rect x="158" y="59" width="9" height="50" fill="var(--sky)"/>
    <g fill="#fff" font-size="2.6" text-anchor="middle" font-family="Work Sans"><text x="36.5" y="89">4.3</text><text x="54.5" y="100">2.4</text><text x="72.5" y="90">4.2</text><text x="90.5" y="88">4.5</text><text x="108.5" y="94">3.5</text><text x="126.5" y="78">6.2</text><text x="144.5" y="73">7.1</text><text x="162.5" y="63">8.9</text></g>
    <g fill="#666" font-size="3.2" text-anchor="middle" font-family="Work Sans"><text x="36.5" y="116">2010</text><text x="54.5" y="116">2011</text><text x="72.5" y="116">2012</text><text x="90.5" y="116">2013</text><text x="108.5" y="116">2014</text><text x="126.5" y="116">2015</text><text x="144.5" y="116">2016</text><text x="162.5" y="116">2017</text></g>
    <circle cx="220" cy="40" r="5" fill="none" stroke="var(--royal)" stroke-width=".6"/><path d="M217.5 40l2 2 3-3.5" fill="none" stroke="var(--royal)" stroke-width=".6"/>
    <circle cx="220" cy="88" r="5" fill="none" stroke="var(--royal)" stroke-width=".6"/><path d="M217 88h6M220 85v6" stroke="var(--royal)" stroke-width=".6"/>
  </svg>
  <div class="abs" style="left:175px;top:48px;width:90px;text-align:center"><div style="font-size:6px;font-weight:600">we are <span class="acc">growing</span></div><div class="tiny" style="font-size:2.8px;margin-top:2px">lorem ipsum dolor sit amet, consectetuer adipiscing elit. maecenas</div></div>
  <div class="abs" style="left:175px;top:96px;width:90px;text-align:center"><div style="font-size:6px;font-weight:600"><span class="acc">join</span> the crew</div><div class="tiny" style="font-size:2.8px;margin-top:2px">lorem ipsum dolor sit amet, consectetuer adipiscing elit. maecenas</div></div>
  <div class="pg">19</div>
</section>

<section class="slide c4 r5">
  <svg class="mark" viewBox="0 0 26 10"><path d="M0 0h14L8 10H0z" fill="var(--ink)"/><path d="M17 0h4l-6 10h-4z" fill="var(--sky)"/></svg>
  <div class="title">Graph <span>Chart</span></div>
  <div class="lede">Lorem ipsum dolor sit amet, consectetuer adipiscing elit. Maecenas porttitor congue massa.</div>
  <div class="brand"><i></i>TIREM</div>
  <svg class="abs" style="left:0;top:0" width="282" height="159" viewBox="0 0 282 159">
    <g fill="#777" font-size="3.3" font-family="Work Sans" text-anchor="end"><text x="14" y="40">6</text><text x="14" y="54">5</text><text x="14" y="67">4</text><text x="14" y="81">3</text><text x="14" y="94">2</text><text x="14" y="108">1</text><text x="14" y="121">0</text></g>
    <line x1="18" y1="120" x2="165" y2="120" stroke="#ccc" stroke-width=".4"/>
    <rect x="40" y="62" width="7" height="58" fill="var(--navy)"/><rect x="47" y="86" width="7" height="34" fill="#6a7488"/><rect x="54" y="60" width="7" height="60" fill="var(--sky)"/>
    <rect x="86" y="52" width="7" height="68" fill="var(--navy)"/><rect x="93" y="73" width="7" height="47" fill="#6a7488"/><rect x="100" y="80" width="7" height="40" fill="var(--sky)"/>
    <rect x="132" y="88" width="7" height="32" fill="var(--navy)"/><rect x="139" y="60" width="7" height="60" fill="#6a7488"/><rect x="146" y="80" width="7" height="40" fill="var(--sky)"/>
    <g fill="#555" font-size="3.3" text-anchor="middle" font-family="Work Sans"><text x="50" y="128">category 1</text><text x="96" y="128">category 2</text><text x="142" y="128">category 3</text></g>
    <circle cx="210" cy="53" r="6" fill="var(--royal)"/><circle cx="210" cy="83" r="6" fill="#6a7488"/><circle cx="210" cy="113" r="6" fill="var(--sky)"/>
    <g fill="none" stroke="#fff" stroke-width=".6"><rect x="207.5" y="51" width="5" height="4"/><rect x="207.5" y="81" width="5" height="4"/><rect x="207.5" y="111" width="5" height="4"/></g>
  </svg>
  <div class="abs" style="left:220px;top:48px"><div class="h" style="font-size:4.3px">option one</div><div class="tiny" style="font-size:2.7px;margin-top:2px;width:50px">Lorem ipsum dolor sit amet, consectetuer adipiscing elit.</div></div>
  <div class="abs" style="left:220px;top:78px"><div class="h" style="font-size:4.3px">option two</div><div class="tiny" style="font-size:2.7px;margin-top:2px;width:50px">Lorem ipsum dolor sit amet, consectetuer adipiscing elit.</div></div>
  <div class="abs" style="left:220px;top:108px"><div class="h" style="font-size:4.3px">option three</div><div class="tiny" style="font-size:2.7px;margin-top:2px;width:50px">Lorem ipsum dolor sit amet, consectetuer adipiscing elit.</div></div>
  <div class="pg">20</div>
</section>

<section class="slide c1 r6">
  <svg class="mark" viewBox="0 0 26 10"><path d="M0 0h14L8 10H0z" fill="var(--ink)"/><path d="M17 0h4l-6 10h-4z" fill="var(--sky)"/></svg>
  <div class="title">Overview <span>Chart</span></div>
  <div class="lede">Lorem ipsum dolor sit amet, consectetuer adipiscing elit. Maecenas porttitor congue massa.</div>
  <div class="brand"><i></i>TIREM</div>
  <svg class="abs" style="left:0;top:0" width="282" height="159" viewBox="0 0 282 159">
    <g fill="#999" font-size="4.5" font-family="Work Sans" text-anchor="middle"><text x="50" y="57">Sales</text><text x="138" y="55">Demand</text><text x="225" y="55">Statistic</text></g>
    <g fill="#999" font-size="2.6" font-family="Work Sans"><text x="10" y="62">40</text><text x="10" y="71">30</text><text x="10" y="80">20</text><text x="10" y="89">10</text><text x="12" y="98">0</text></g>
    <path d="M18 68L48 68 60 75 92 72 92 97 18 97z" fill="var(--sky)"/>
    <path d="M18 86L48 86 62 80 92 66 92 97 18 97z" fill="var(--green)"/>
    <g fill="#999" font-size="2.6" font-family="Work Sans"><text x="16" y="103">may</text><text x="33" y="103">jun</text><text x="49" y="103">jul</text><text x="64" y="103">aug</text><text x="82" y="103">sep</text></g>
    <line x1="100" y1="97" x2="178" y2="97" stroke="#ccc" stroke-width=".4"/>
    <rect x="104" y="74" width="7" height="23" fill="var(--blue)"/><rect x="111" y="84" width="7" height="13" fill="var(--navy)"/>
    <rect x="122" y="80" width="7" height="17" fill="var(--blue)"/><rect x="129" y="66" width="7" height="31" fill="var(--navy)"/>
    <rect x="140" y="78" width="7" height="19" fill="var(--blue)"/><rect x="147" y="86" width="7" height="11" fill="var(--navy)"/>
    <rect x="158" y="68" width="7" height="29" fill="var(--blue)"/><rect x="165" y="82" width="7" height="15" fill="var(--navy)"/>
    <g fill="#999" font-size="2.6" font-family="Work Sans"><text x="106" y="103">may</text><text x="125" y="103">jun</text><text x="143" y="103">jul</text><text x="160" y="103">aug</text></g>
    <line x1="192" y1="97" x2="262" y2="97" stroke="#ccc" stroke-width=".4"/>
    <path d="M196 72C210 60 218 88 232 80S252 62 262 66" fill="none" stroke="var(--blue)" stroke-width=".8"/>
    <path d="M196 84C210 60 220 70 232 78S252 92 262 74" fill="none" stroke="var(--green)" stroke-width=".8"/>
    <g fill="#999" font-size="2.6" font-family="Work Sans"><text x="196" y="103">may</text><text x="216" y="103">jun</text><text x="234" y="103">jul</text><text x="252" y="103">aug</text></g>
    <g fill="none" stroke="var(--sky)" stroke-width=".6"><rect x="27" y="133" width="2" height="5"/><rect x="30.5" y="130" width="2" height="8"/><rect x="34" y="128" width="2" height="10"/><rect x="37.5" y="131" width="2" height="7"/></g>
  </svg>
  <div class="abs tiny" style="left:60px;top:128px;width:200px;font-size:2.8px">It was popularised in the 1960s with the release of sheets containing Lorem Ipsum passages, and more recently with desktop publishing software including versions of Lorem Ipsum.</div>
  <div class="pg">21</div>
</section>

<section class="slide c2 r6">
  <svg class="mark" viewBox="0 0 26 10"><path d="M0 0h14L8 10H0z" fill="var(--ink)"/><path d="M17 0h4l-6 10h-4z" fill="var(--sky)"/></svg>
  <div class="title">World <span>Maps</span></div>
  <div class="lede">Lorem ipsum dolor sit amet, consectetuer adipiscing elit. Maecenas porttitor congue massa.</div>
  <div class="brand"><i></i>TIREM</div>
  <div class="photo" role="img" aria-label="World map in light grey with North America highlighted in blue and China in green" style="left:25px;top:52px;width:150px;height:85px;background:radial-gradient(ellipse at 50% 45%,#e4e6ea 0%,#eef0f2 55%,#fff 75%)"></div>
  <svg class="abs" style="left:226px;top:37px" width="14" height="12" viewBox="0 0 14 12"><path d="M7 1v9M3 10h8M4 5a4 4 0 0 1 7-2" fill="none" stroke="var(--green)" stroke-width=".7"/></svg>
  <div class="abs" style="left:185px;top:53px;width:92px;text-align:center"><div style="font-size:6px;font-weight:600">we are <span class="grn">growing</span></div><div class="tiny" style="font-size:2.8px;margin-top:2px">lorem ipsum dolor sit amet, consectetuer adipiscing elit. maecenas</div></div>
  <svg class="abs" style="left:226px;top:86px" width="14" height="12" viewBox="0 0 14 12"><path d="M2 4h8a2 2 0 1 0-2-2M2 7h10M2 10h7" fill="none" stroke="var(--blue)" stroke-width=".7"/></svg>
  <div class="abs" style="left:185px;top:102px;width:92px;text-align:center"><div style="font-size:6px;font-weight:600"><span class="acc">join</span> the crew</div><div class="tiny" style="font-size:2.8px;margin-top:2px">lorem ipsum dolor sit amet, consectetuer adipiscing elit. maecenas</div></div>
</section>

<section class="slide c3 r6">
  <svg class="mark" viewBox="0 0 26 10"><path d="M0 0h14L8 10H0z" fill="var(--ink)"/><path d="M17 0h4l-6 10h-4z" fill="var(--sky)"/></svg>
  <div class="title">US <span>Maps</span></div>
  <div class="lede">Lorem ipsum dolor sit amet, consectetuer adipiscing elit. Maecenas porttitor congue massa.</div>
  <div class="brand"><i></i>TIREM</div>
  <div class="abs" style="left:23px;top:48px;width:85px;font-size:4.3px;line-height:1.3;color:#333">Ut wisi enim ad minim veniam, quis nostrud exerci</div>
  <div class="abs tiny" style="left:23px;top:64px;width:85px;font-size:2.8px;color:#555"><b>Ut wisi enim</b> ad minim veniam, quis nostrud exerci tation ullamcorper nibh euismod tincidunt ut laoreet dolore magna aliquam erat volutpat. Ut wisi enim ad minim veniam, quis nostrud exerci tation ullamcorper nibh euismod tincidunt ut laoreet</div>
  <div class="photo" role="img" aria-label="Map of the United States in grey with location pins" style="left:130px;top:40px;width:135px;height:100px;background:radial-gradient(ellipse at 50% 50%,#cfd1d5 0%,#dcdee1 55%,#fff 72%)"></div>
  <div class="abs" style="left:182px;top:35px;width:78px;height:12px;background:var(--blue);clip-path:polygon(4% 0,100% 0,96% 100%,0 100%);color:#fff;padding:2.5px 0 0 5px;font-size:5px;font-weight:600">70%<span style="font-size:2.2px;font-weight:400;margin-left:4px;display:inline-block;width:40px;vertical-align:middle;line-height:1.2">Ut wisi enim ad minim veniam, quis nostrud exerci tation</span></div>
  <svg class="abs" style="left:0;top:0" width="282" height="159" viewBox="0 0 282 159">
    <g fill="none" stroke="#333" stroke-width=".6"><path d="M191 66a2.5 2.5 0 1 1 5 0c0 2-2.5 4-2.5 4s-2.5-2-2.5-4z" stroke="var(--blue)"/><path d="M151 79a2.5 2.5 0 1 1 5 0c0 2-2.5 4-2.5 4s-2.5-2-2.5-4z"/><path d="M174 105a2.5 2.5 0 1 1 5 0c0 2-2.5 4-2.5 4s-2.5-2-2.5-4z"/><path d="M231 111a2.5 2.5 0 1 1 5 0c0 2-2.5 4-2.5 4s-2.5-2-2.5-4z"/></g>
  </svg>
  <div class="pg">23</div>
</section>

<section class="slide c4 r6">
  <svg class="abs" style="left:0;top:0" width="282" height="159" viewBox="0 0 282 159">
    <polygon points="170,0 282,0 282,40 240,40" fill="var(--navy)"/>
    <polygon points="70,159 110,110 282,110 282,159" fill="var(--navy)"/>
  </svg>
  <div class="photo" role="img" aria-label="Sailing yacht seen from above on blue-green water" style="left:29px;top:27px;width:226px;height:104px;background:linear-gradient(160deg,var(--navy),#1d5a8c 55%,var(--green))"></div>
  <svg class="abs" style="left:113px;top:42px" width="56" height="50" viewBox="0 0 56 50"><circle cx="28" cy="25" r="23" fill="none" stroke="rgba(255,255,255,.5)" stroke-width="1.5"/></svg>
  <div class="abs" style="left:29px;top:98px;width:226px;text-align:center;font:italic 700 10px/1 Poppins,sans-serif;color:#fff">Thank <span class="grn">You</span></div>
  <div class="abs" style="left:29px;top:110px;width:226px;text-align:center;font-size:3.2px;color:#dfe6f5">Lorem ipsum is simply dummy text of<br>the printing and typesetting industry</div>
  <div class="social" style="left:224px;top:144px"><i></i><i></i><i></i><i></i></div>
</section>

</div>
</body>
</html>
```